Business Card Design

Divorce
Collaborative Family Law
Family Dispute Resolution
Family Law Property & Children

Target Market(s)

Australia

Industry/Entity Type

Business

Contact Information for Business Card

Delphine Hartwell
M Laws (Family Practice) LLB (Hons) BA (Hons) Grad Dip Med
Family Dispute Resolution Provider
Hartwell Family Law
PO Box 4723 Ferncliff 3792
Phone 03 58217000 Fax 03 58217100 Email hartwellfamilylaw@quillnet.example

Colors
f04a51

Requirements
Should not have
• Any reference to
United States or US terminology
the word Company

```html
<!DOCTYPE html>
<html lang="en">
<head>
<meta charset="utf-8">
<title>Hartwell Family Law – Business Card</title>
<link rel="stylesheet" href="https://fonts.googleapis.com/css2?family=Cinzel:wght@700&family=Fondamento&family=Noto+Serif:wght@600&display=swap">
<style>
  :root {
    --canvas: #ecebe8;
    --card-red: #f04a51;
    --card-red-light: #f58a86;
    --swoosh-red: #e0242c;
    --blue-dark: #2a5878;
    --blue-mid: #5f7f98;
    --blue-light: #f2f4f6;
    --name-yellow: #ffe22a;
    --text-white: #ffffff;
    --silhouette: #141212;
  }
  * { box-sizing: border-box; margin: 0; padding: 0; }
  html, body {
    width: 1200px; height: 1200px; overflow: hidden;
    background: var(--canvas);
  }
  .stage {
    width: 1200px; height: 1200px;
    display: flex; align-items: center; justify-content: center;
  }
  .card {
    position: relative;
    width: 1080px; height: 668px;
    background: radial-gradient(ellipse 60% 70% at 55% 40%, var(--card-red-light) 0%, var(--card-red) 70%);
    overflow: hidden;
    box-shadow: 0 6px 24px rgba(0,0,0,0.18);
  }
  .card-art { position: absolute; inset: 0; width: 100%; height: 100%; }
  .identity { position: absolute; left: 74px; top: 74px; }
  .holder-name {
    font-family: "Cinzel", serif;
    font-weight: 700;
    font-size: 35px;
    letter-spacing: 1px;
    color: var(--name-yellow);
    line-height: 1.1;
  }
  .credentials, .role {
    font-family: "Fondamento", cursive;
    font-size: 23px;
    color: var(--text-white);
    line-height: 1.55;
    white-space: nowrap;
  }
  .credentials { margin-top: 14px; }
  .contact {
    position: absolute; left: 55px; top: 432px;
    font-family: "Noto Serif", serif;
    font-weight: 600;
    font-size: 22px;
    color: var(--text-white);
    list-style: none;
    white-space: nowrap;
  }
  .contact li { line-height: 44.5px; }
</style>
</head>
<body>
<main class="stage">
  <section class="card">
    <svg class="card-art" viewBox="0 0 1080 668" preserveAspectRatio="none">
      <defs>
        <linearGradient id="blueField" x1="1" y1="0" x2="0.3" y2="1">
          <stop offset="0" stop-color="var(--blue-light)"/>
          <stop offset="0.35" stop-color="var(--blue-mid)"/>
          <stop offset="0.75" stop-color="var(--blue-dark)"/>
        </linearGradient>
        <linearGradient id="photoFade" x1="0" y1="0" x2="0" y2="1">
          <stop offset="0" stop-color="#f7a29c" stop-opacity="0.2"/>
          <stop offset="0.6" stop-color="#e6585a" stop-opacity="0.4"/>
          <stop offset="1" stop-color="#f07a6a" stop-opacity="0.3"/>
        </linearGradient>
        <linearGradient id="silhouetteFade" x1="0" y1="0" x2="0" y2="1">
          <stop offset="0" stop-color="var(--silhouette)" stop-opacity="0.9"/>
          <stop offset="0.85" stop-color="var(--silhouette)" stop-opacity="0.95"/>
          <stop offset="1" stop-color="var(--silhouette)" stop-opacity="0.3"/>
        </linearGradient>
      </defs>

      <rect class="background-photo" x="110" y="150" width="650" height="518" rx="40"
            fill="url(#photoFade)" role="img"
            aria-label="Faded sunset photograph of a family walking hand in hand"/>

      <path class="blue-field" d="M856,0 C925,150 905,420 505,668 L1080,668 L1080,0 Z" fill="url(#blueField)"/>
      <path class="red-swoosh" d="M846,0 C908,150 880,410 455,668 L505,668 C905,420 925,150 856,0 Z" fill="var(--swoosh-red)"/>

      <rect class="family-silhouette" x="722" y="215" width="324" height="420" rx="60"
            fill="url(#silhouetteFade)" role="img"
            aria-label="Dark silhouette illustration of a family of four walking together"/>
    </svg>

    <header class="identity">
      <h1 class="holder-name">DELPHINE HARTWELL</h1>
      <p class="credentials">M Laws (Family Practice) LLB (Hons) BA (Hons) Grad Dip Med</p>
      <p class="role">Family Dispute Resolution Provider</p>
    </header>

    <ul class="contact">
      <li class="contact-address">Hartwell Family Law PO Box 4723 Ferncliff 3792</li>
      <li class="contact-phone">Phone : 03 58217000</li>
      <li class="contact-fax">Fax : 03 58217100</li>
      <li class="contact-email">Email : hartwellfamilylaw@quillnet.example</li>
    </ul>
  </section>
</main>
</body>
</html>
```